Flyer für Therapie- und Gesundheitsdienstleister
Zielgruppe
Therapie- und Gesundheitsdienstleister im Bereich Physiotherapie, Podologie, Prävention und betriebliche Gesundheitsförderung. Für dieses Projekt möchten wir einen Flyer erstellen lassen für die Bewerbung der betrieblichen Gesundheitsförderungen in bzw. für Firmen
Aufgabenstellung
Klare Strukturen, nicht verspielt, DINA4 oder DINA5; leicht medizinischer Touch, evntuell Stockfotos integrieren, edel und hochwertiges Design

```html
<!DOCTYPE html>
<html lang="de">
<head>
<meta charset="utf-8">
<title>Forum Vitalis – Betriebliche Gesundheitsförderung</title>
<link href="https://fonts.googleapis.com/css2?family=Montserrat:wght@400;500;600;700&display=swap" rel="stylesheet">
<style>
:root{
  --orange:#ec7410;
  --ink:#1d1d1d;
  --grey:#5a5a5a;
  --tab:#4a4a4a;
  --box:#efefef;
  --photo-a:#c9d6dc;
  --photo-b:#eef2f3;
  --paper:#ffffff;
}
*{box-sizing:border-box;margin:0;padding:0}
html,body{width:1200px;height:806px;overflow:hidden;background:#fff;font-family:'Montserrat',sans-serif;color:var(--ink)}
.canvas{position:relative;width:1200px;height:806px}
.page{position:absolute;top:39px;width:513px;height:726px;background:var(--paper);overflow:hidden;box-shadow:0 4px 14px rgba(0,0,0,.22)}
.page--front{left:47px}
.page--back{left:639px}
.abs{position:absolute}

.badge{position:absolute;border-radius:50%;background:var(--orange);color:#fff;font-weight:700;text-align:center;display:flex;align-items:center;justify-content:center;line-height:1.3;box-shadow:0 3px 8px rgba(0,0,0,.25)}
.badge span{transform:rotate(-5deg);display:block}

.hero-photo{position:absolute;left:0;top:0}
.brand{position:absolute;left:236px;top:74px;display:flex;align-items:center;gap:12px}
.brand-dot{width:74px;height:74px;border-radius:50%;background:var(--orange);opacity:.9}
.brand-name{font-weight:500;font-size:30px;line-height:1.1;color:#555}

.headline{position:absolute;left:0;width:100%;top:362px;text-align:center;color:var(--orange);font-weight:700;font-size:20.5px}
.intro{position:absolute;left:30px;width:453px;top:396px;text-align:center;font-size:12.3px;line-height:17.2px;color:#444}
.intro b{color:var(--ink);font-weight:700}

.info-box{position:absolute;left:24px;top:468px;width:204px;height:200px;background:var(--box);border-radius:8px;box-shadow:0 2px 6px rgba(0,0,0,.15);padding:14px 11px;font-size:8.6px;line-height:12.5px}
.point{display:flex;align-items:center;gap:8px;font-weight:600;margin-top:14px}
.point-num{flex:none;width:20px;height:20px;border-radius:50%;background:var(--orange);color:#fff;font-weight:700;font-size:10px;display:flex;align-items:center;justify-content:center}
.info-box .outro{margin-top:16px}

.body-text{position:absolute;left:248px;top:468px;width:246px;font-size:8.6px;line-height:12.9px}
.body-text .strong{margin-top:12px;font-weight:700}

.footer-tab{position:absolute;bottom:0;left:178px;width:157px;height:27px;background:var(--tab);border-radius:6px 6px 0 0;color:#fff;font-weight:600;font-size:8.6px;display:flex;align-items:center;justify-content:center}

.back-photo{position:absolute;left:0;top:0;width:513px;height:131px;background:linear-gradient(90deg,#d9dde0 0%,#b9bfc4 40%,#e7d3cb 70%,#f1e3dc 100%)}
.section-title{position:absolute;left:29px;top:144px;font-size:18px;font-weight:700;color:#3c3c3c}
.col{position:absolute;top:176px;font-size:8.6px;line-height:12.9px}
.col--left{left:29px;width:240px}
.col--right{left:284px;width:210px}
.col h3{color:var(--orange);font-size:10.6px;font-weight:700;margin-bottom:7px}
.col p{margin-bottom:12px}
.checks{list-style:none;margin-bottom:13px}
.checks li{position:relative;padding-left:11px;margin-bottom:4px}
.checks li::before{content:"✓";position:absolute;left:0;top:0;font-weight:700}

.cost-box{position:absolute;left:19px;top:535px;width:309px;height:146px;background:var(--box);border-radius:8px;box-shadow:0 2px 6px rgba(0,0,0,.15);padding:8px 12px;font-size:8.6px;line-height:12.9px}
.cost-box h2{font-size:17.5px;font-weight:600;color:#3c3c3c;margin-bottom:4px}
.cost-box p{margin-bottom:2px}

.contact-photo{position:absolute;left:352px;top:521px;width:67px;height:79px;border-radius:4px;background:linear-gradient(180deg,#d6d8d9,#a8b8a0)}
.contact{position:absolute;left:352px;top:608px;font-size:8.6px;line-height:10.6px;color:#555}
.contact b{color:#333;font-weight:700}
.contact .gap{margin-top:9px}
</style>
</head>
<body>
<div class="canvas">

  <section class="page page--front">
    <svg class="hero-photo" width="513" height="360" viewBox="0 0 513 360" role="img" aria-label="Foto: zwei Kolleginnen geben sich lachend ein High-Five im hellen Büro">
      <defs>
        <linearGradient id="heroFill" x1="0" y1="0" x2="1" y2="0.4">
          <stop offset="0" stop-color="#b7c3c7"/>
          <stop offset="0.45" stop-color="#d3dde0"/>
          <stop offset="1" stop-color="#eef2f2"/>
        </linearGradient>
      </defs>
      <path d="M0 0H513V210Q330 350 0 300Z" fill="url(#heroFill)"/>
      <path d="M513 212Q360 338 180 340Q330 330 513 226Z" fill="#9a9a9a" opacity=".8"/>
    </svg>
    <div class="brand">
      <div class="brand-dot"></div>
      <div class="brand-name">Forum<br>Vitalis</div>
    </div>
    <div class="badge" style="left:374px;top:237px;width:100px;height:100px;font-size:10px"><span>Jetzt einen<br>persönlichen<br>Termin<br>vereinbaren!</span></div>

    <h1 class="headline">Betriebliche Gesundheitsförderung</h1>
    <p class="intro">Die betriebliche Gesundheitsförderung hat das Ziel die <b>Gesundheit der Mitarbeiter</b> zu erhalten und zu fördern sowie die <b>Leistungsfähigkeit und Motivation</b> der Belegschaft zu steigern.</p>

    <div class="info-box">
      <p>Immer mehr gewinnen jedoch folgende Punkte an Bedeutung für Unternehmen:</p>
      <div class="point" style="margin-top:16px"><span class="point-num">1.</span>Mitarbeiterbindung &amp;</div>
      <div class="point"><span class="point-num">2.</span>Arbeitgeber Attraktivität zu erhöhen, um ein Vorteil am Bewerbermarkt zu erzielen.</div>
      <p class="outro">Auch da können wir Sie mit unserem Know-How und abgerundeten Konzept unterstützen.</p>
    </div>

    <div class="body-text">
      <p>In regelmäßigen Abständen setzen wir uns mit Ihren Mitarbeitern in Verbindung und erfragen den jeweiligen IST Stand und besprechen gemeinsames Vorgehen, um gesundheitliche Problematiken im Handlungsfeld Bewegung und Entspannung präventiv vorzubeugen. Ihre Mitarbeiter werden dadurch in festen monatlichen Intervallen sensibilisiert dass Sie sich um das Wohlbefinden Ihrer Mitarbeiter kümmern und Sie auch darin investieren.</p>
      <p class="strong">Sie als Arbeitgeber können nicht wissen und auch zeitlich nicht gewährleisten welche individuellen gesundheitlichen Problematiken Ihre Mitarbeiter haben. Deshalb bieten wir Ihnen eine individuelle Lösung an Dienstleistung, welche den individuellen Bedarf Ihrer Mitarbeiter deckt.</p>
    </div>

    <div class="footer-tab">www.physio-wellenrath.de</div>
  </section>

  <section class="page page--back">
    <div class="back-photo" role="img" aria-label="Foto: lächelnde Therapeutin im Trainingsraum mit Geräten"></div>
    <div class="badge" style="left:20px;top:-7px;width:98px;height:98px;font-size:10px"><span>Jetzt einen<br>persönlichen<br>Termin<br>vereinbaren!</span></div>

    <h2 class="section-title">Unsere Leistungen</h2>

    <div class="col col--left">
      <h3>Messung &amp; Analysen</h3>
      <ul class="checks">
        <li>Messung &amp; Analysen zur individuellen Stress- und Resilienzdiagnostik um zielorientiert ein Stressmanagment in Ihrem Betrieb zu implementieren.</li>
        <li>Dokumentation von Körperdaten und Risikofaktoren in einer Eingangskontrolle und einem ½ jährlichen Wiederholung der Kontrolle.</li>
        <li>Wirbelsäulen- und Haltungsscreenings, Haltung, Beweglichkeit und Haltungskomponenten werden anschaulich dargestellt und bilden die Basis für zielführende Visualisierung und fundierte Übungsempfehlung.</li>
        <li>Analysen von Körperstabilität und Gleichgewicht; BalanceScan Pro ist ein erprobtes Analysetool für das Thema Körperstabilität</li>
      </ul>
      <h3>Mentale Gesundheit</h3>
      <p>Programme zur Achtsamkeit, Entspannung, und Wahrnehmung. In Kleingruppen, Online</p>
      <h3>Gesundheitstage für Firmen</h3>
      <p>Individuell auf Ihre Firma abgestimmt.</p>
    </div>

    <div class="col col--right">
      <h3>Bewegungsprogramme:</h3>
      <p style="margin-bottom:6px">Präventionsprogramme nach §20 zertifiziert von den Krankenkassen wie zum Beispiel:</p>
      <ul class="checks">
        <li>Entspannungskurse Hatha Yoga</li>
        <li>Pilates</li>
        <li>Rückengymnastik</li>
        <li>Ganzkörper Training an Geräten</li>
        <li>Fit am Arbeitsplatz</li>
        <li>Online-Präventionskurs<br>(zeitlich und räumlich unabhängig)</li>
        <li>und einige mehr....</li>
      </ul>
      <h3>Digitaler Gesundheitscoach</h3>
      <ul class="checks">
        <li>Workouts</li>
        <li>Live Online- Kurse</li>
        <li>Physio Übungen gezielt und individuell in der Einzelberatung online und persönlich abgestimmt</li>
        <li>Online Präventionscoach<br>oder als Einzelleistung buchbar</li>
        <li>Online Präventionscoach</li>
      </ul>
    </div>

    <div class="cost-box">
      <h2>Informationen zu den Kosten</h2>
      <p>Bis zu 600 € können Sie, als Arbeitgeber steuerfrei bezuschussen. Voraussetzung dafür ist, dass die fachlichen Anforderungen des GKV- Spitzenverbandes erfüllt werden.</p>
      <p>Diese Leistungen können wir erfüllen und einige mehr on Top. Lassen Sie sich persönlich und individuell beraten und nehmen Sie persönlich oder via E-Mail Kontakt mit uns auf. Senden Sie uns eine E-Mail an berger@physio-wellenrath.de und wir melden uns umgehend für eine kostenlose Beratung.</p>
    </div>

    <div class="contact-photo" role="img" aria-label="Porträtfoto der Ansprechpartnerin"></div>
    <div class="contact">
      <b>Ihre Ansprechpartnerin<br>Katrin Berger</b>
      <div class="gap"><b>Physio Wellenrath</b><br>Lindenallee 57b<br>46499 Wellenrath</div>
      <div class="gap" style="margin-top:4px">02851 - 48 21 93<br>berger@physio-wellenrath.de</div>
    </div>

    <div class="footer-tab">www.physio-wellenrath.de</div>
  </section>

</div>
</body>
</html>
```